Plakat-Design für eine Budgetplanung für ein Kinderbuch
Das vorgeschlagene Poster war von Anfang an unser Favorit. Es zeichnet sich aus, durch ein ansprechendes, klares und kindgerechtes Design. Wir haben die ausgesprochen zuverlässige Arbeit und Kommunikation sehr geschätzt und hoffen auf weitere Zusammenarbeit.
Zielgruppe
Wir sind ein Verlag und bringen nächsten Monat zwei Kinder-/Jugendbücher mit dem Thema Finanzbildung heraus. Das Alter der Zielgruppe ist zwischen 8 und 13 Jahren. Zu den Büchern gehört ein hochwertiges Posterset aus drei Postern. In diesem Auftrag soll zunächst das erste Poster designed werden. Hier geht es darum eine kleine 'Budgetplanung' zu erstellen. In weiteren Aufträgen sollen auch Illustrationen aufgewertet und Designs für Websites erstellt werden.
Aufgabenstellung
Wir werden einige Bilder bereitstellen, die verarbeitet werden dürfen (es müssen nicht alle verwendet werden!). Es wäre schön, wenn das Posterdesign so ausgelegt wird, dass die Bilder gut in das Gesamtdesign passen. Die Bildqualität des Posters soll auf DINA2 optimiert sein. Weiterhin stellen wir einen 'Beispiel-Geldplan' zur Verfügung, der alle Texte enthält, die das Poster beinhalten soll. Das Design dieses Beispiel-Geldplans soll unberücksichtigt bleiben. Das Gesamtdesign soll hochwertig und kreativ sein.

```html
<!DOCTYPE html>
<html lang="de">
<head>
<meta charset="utf-8">
<title>Wie ich mir meine Träume erfülle – Geldplan-Poster</title>
<link rel="stylesheet" href="https://fonts.googleapis.com/css2?family=Bangers&family=Poppins:wght@300&display=swap">
<style>
  :root{
    --navy:#123a8a;
    --teal:#00a09a;
    --teal-deep:#01939a;
    --mint:#6fc29a;
    --magenta:#8e1f6c;
    --night:#302a4a;
    --white:#ffffff;
    --page:#ffffff;
  }
  html,body{margin:0;padding:0;width:1200px;height:1200px;overflow:hidden;background:var(--page);}
  .poster{
    position:absolute;left:216px;top:55px;width:1240px;height:1755px;
    transform:scale(0.625);transform-origin:0 0;overflow:hidden;
    box-shadow:0 12px 30px rgba(0,0,0,.18);
    color:var(--white);
    font-family:"Poppins",sans-serif;font-weight:300;
  }
  .band{position:absolute;left:0;width:1240px;}
  .band--header{top:0;height:292px;background:linear-gradient(90deg,var(--navy) 0%,#055a96 35%,var(--teal) 80%,var(--teal) 100%);}
  .band--income{top:292px;height:293px;background:linear-gradient(90deg,var(--mint) 0%,var(--teal) 40%,var(--teal-deep) 100%);}
  .band--expenses{top:585px;height:293px;background:linear-gradient(90deg,var(--teal) 0%,var(--teal) 30%,#5a7b8e 60%,var(--magenta) 100%);}
  .band--plans{top:878px;height:292px;background:linear-gradient(90deg,var(--teal-deep) 0%,var(--teal-deep) 40%,#5a6a8a 65%,var(--magenta) 100%);}
  .band--savings{top:1170px;height:292px;background:linear-gradient(90deg,var(--teal-deep) 0%,var(--teal-deep) 35%,#0c5f70 65%,var(--night) 100%);}
  .band--dreams{top:1462px;height:293px;background:linear-gradient(90deg,var(--mint) 0%,var(--teal) 35%,#0b6a78 60%,var(--night) 100%);}

  .headline{font-family:"Bangers",sans-serif;font-weight:400;letter-spacing:1px;line-height:1;margin:0;position:absolute;white-space:nowrap;}
  .copy{position:absolute;margin:0;font-size:43px;line-height:57px;white-space:nowrap;}

  .title-lead{position:absolute;left:94px;top:136px;font-size:45px;}
  .title-main{left:462px;top:92px;font-size:104px;}

  .income-head{left:88px;top:322px;font-size:54px;}
  .income-list{left:88px;top:378px;}

  .expenses-head{right:90px;top:665px;font-size:54px;}
  .expenses-note{right:90px;top:722px;text-align:right;}

  .plans-list{left:88px;top:922px;font-size:54px;line-height:70px;}

  .savings-head{right:90px;top:1283px;font-size:54px;}

  .dreams-head{left:88px;top:1530px;font-size:84px;line-height:82px;}

  .art{position:absolute;}
  .art--teacher{left:775px;top:225px;width:270px;height:410px;border-radius:40% 40% 35% 35%;background:linear-gradient(180deg,#f3d36a 0%,#f6f1e6 30%,#6fb6e8 60%,#4a9ad8 100%);}
  .art--banknote{left:38px;top:617px;width:484px;height:233px;background:linear-gradient(90deg,#a7d6bc 0%,#9fcf8a 50%,#e8c84a 75%,#a7d6bc 100%);border:3px solid #4a7a3a;}
  .art--euro{left:745px;top:820px;width:275px;height:410px;border-radius:45% 45% 40% 40%;background:linear-gradient(180deg,#f6f1e6 0%,#ea7a48 35%,#e2773f 100%);}
  .art--piggy{left:38px;top:1160px;width:470px;height:355px;border-radius:45% 45% 40% 40%;background:linear-gradient(180deg,#d88ac0 0%,#b8d23a 35%,#e86070 55%,#f4c6c8 80%,#f0b8bc 100%);}
  .art--treasure{left:625px;top:1555px;width:615px;height:200px;border-radius:50% 40% 0 0;background:linear-gradient(90deg,#3a7ad0 0%,#f2e23a 25%,#f6e63c 65%,#8ac04a 82%,#c8509a 100%);}
</style>
</head>
<body>
<main class="poster">
  <section class="band band--header"></section>
  <section class="band band--income"></section>
  <section class="band band--expenses"></section>
  <section class="band band--plans"></section>
  <section class="band band--savings"></section>
  <section class="band band--dreams"></section>

  <p class="title-lead">Wie ich mir meine</p>
  <h1 class="headline title-main">TRÄUME ERFÜLLE</h1>

  <h2 class="headline income-head">ICH ERHALTE JEDEN MONAT</h2>
  <p class="copy income-list">Davon Taschengeld<br>Aus meinem Verdienst<br>Durch meine Investition</p>

  <h2 class="headline expenses-head">ICH BRAUCHE JEDEN MONAT</h2>
  <p class="copy expenses-note">(für Freizeit, Essen etc.)</p>

  <h2 class="headline plans-list">ICH MÖCHTE SPAREN<br>ICH MÖCHTE INVESTIEREN<br>ICH MÖCHTE SPENDEN</h2>

  <h2 class="headline savings-head">WIE VIEL ICH SCHON GESPART HABE</h2>

  <h2 class="headline dreams-head">MEINE TRÄUME GEHEN<br>IN ERFÜLLUNG</h2>

  <div class="art art--teacher" role="img" aria-label="Illustration: blaue Comicfigur mit Brille an einer Tafel mit Formeln, darüber Glühbirnen"></div>
  <div class="art art--banknote" role="img" aria-label="Illustration: gezeichneter Fünfer-Geldschein mit Europakarte und Figurengruppe"></div>
  <div class="art art--euro" role="img" aria-label="Illustration: orange Comicfigur hält ein großes Euro-Zeichen"></div>
  <div class="art art--piggy" role="img" aria-label="Illustration: bunte Comicfiguren auf einem rosa Sparschwein, eine zieht einen Wagen mit Münzen"></div>
  <div class="art art--treasure" role="img" aria-label="Illustration: Comicfiguren baden in einem großen Haufen Goldmünzen"></div>
</main>
</body>
</html>
```